Cobaltine Outdoor Therapy needs Corporate Team Building Brochure

Cobaltine Outdoor Therapy is a new company in Vancouver Canada. We do adventure based counselling, family counselling, groups and team building events. We are looking to expand our marketing to the corporate team building world. What makes us different is that we don't just take people to play games and do adventure activities, we are able to use our training in psychology and coaching to make more of an impact. We would like to see designs that are professional and engaging, something that shows our wild adventure side. Our website is being redone, but to get a sense check out www.cobaltineoutdoor.com

Target Market(s)

Vancouver downtown corporate teams.

Industry/Entity Type

Building

Font styles to use
Serif

Colors
acd037

Requirements
Must have
• some reference (visual or otherwise) to adventure activities, we do rock climbing, sea kayaking, hiking, as well as team building challenge initiatives.
• This is a flyer specifically for our team building services, it is not a general cobaltine outdoor therapy flyer. Use name Cobaltine Outdoor, not Cobaltine Outdoor Therapy

```html
<!DOCTYPE html>
<html lang="en">
<head>
<meta charset="utf-8">
<title>Cobaltine Outdoor – Team Building Brochure</title>
<link rel="stylesheet" href="https://fonts.googleapis.com/css2?family=Montserrat:wght@400;500;600;700&family=Roboto+Condensed:wght@400&display=swap">
<style>
  :root {
    --leaf: #9dca3c;
    --forest: #1d6a3a;
    --deep-green: #2f9e44;
    --olive: #7da831;
    --bark: #3c2318;
    --ink: #1a1a1a;
    --slate: #4f4f4f;
    --mist: #b9b3ae;
    --paper: #ffffff;
    --fold: #ececec;
    --sky: #7fb6cf;
  }
  * { margin: 0; padding: 0; box-sizing: border-box; }
  html, body { width: 1200px; height: 1000px; overflow: hidden; background: var(--paper); }
  .canvas { position: relative; width: 1200px; height: 1000px; font-family: "Montserrat", sans-serif; }
  .artwork { position: absolute; inset: 0; }
  .quote {
    position: absolute; left: 62px; top: 122px; width: 520px;
    font-family: "Roboto Condensed", sans-serif; font-size: 14.6px; line-height: 20.6px; color: var(--ink);
  }
  .quote .mark { color: var(--paper); font-family: "Montserrat", sans-serif; font-weight: 700; font-size: 18px; }
  .quote .mark-open { position: absolute; left: -17px; top: -2px; }
  .founder-name { position: absolute; left: 62px; top: 310px; font-size: 17px; font-weight: 700; color: var(--forest); }
  .founder-role { position: absolute; left: 62px; top: 334px; font-size: 13px; color: var(--slate); }
  .contact-title {
    position: absolute; left: 27px; width: 566px; top: 633px; text-align: center;
    font-size: 34px; font-weight: 600; color: var(--forest);
  }
  .contact-lines {
    position: absolute; left: 27px; width: 566px; top: 704px; text-align: center;
    font-size: 18px; line-height: 26px; color: var(--slate);
  }
  .contact-lines strong { font-weight: 600; color: #444; }
  .web-address {
    position: absolute; left: 27px; width: 566px; top: 856px; text-align: center;
    font-size: 19px; font-weight: 600; color: var(--paper);
  }
  .brand-mark { position: absolute; left: 700px; top: 150px; display: flex; align-items: center; gap: 16px; }
  .brand-dot { width: 70px; height: 70px; border-radius: 50%; background: var(--leaf); }
  .brand-name { font-size: 38px; font-weight: 600; color: var(--leaf); line-height: 1.05; }
  .cover-title {
    position: absolute; left: 608px; width: 567px; top: 802px; text-align: center;
    font-size: 33px; font-weight: 500; color: var(--paper);
  }
  .cover-tagline {
    position: absolute; left: 608px; width: 567px; top: 848px; text-align: center;
    font-size: 14px; line-height: 18px; color: var(--mist);
  }
</style>
</head>
<body>
<div class="canvas">
  <svg class="artwork" width="1200" height="1000" viewBox="0 0 1200 1000">
    <defs>
      <clipPath id="cover-panel"><rect x="608" y="103" width="567" height="795"/></clipPath>
    </defs>

    <!-- back panel -->
    <rect class="panel-back" x="27" y="103" width="566" height="795" fill="var(--paper)"/>
    <polygon class="band-quote" points="27,103 593,103 593,325 27,398" fill="var(--leaf)"/>
    <polygon class="band-footer" points="27,857 593,805 593,898 27,898" fill="var(--bark)"/>
    <rect class="fold-gutter" x="593" y="103" width="15" height="795" fill="var(--fold)"/>
    <circle class="back-emblem" cx="300" cy="520" r="62" fill="none" stroke="var(--leaf)" stroke-width="6"/>

    <!-- cover panel -->
    <g clip-path="url(#cover-panel)">
      <rect x="608" y="103" width="567" height="795" fill="var(--paper)"/>
      <polygon class="band-feature" points="608,325 1175,250 1175,740 608,800" fill="var(--leaf)"/>
      <circle cx="1010" cy="325" r="26" fill="var(--olive)" opacity=".45"/>
      <circle cx="1060" cy="362" r="30" fill="var(--olive)" opacity=".45"/>
      <circle cx="1095" cy="412" r="40" fill="var(--olive)" opacity=".6"/>
      <circle cx="1095" cy="520" r="78" fill="var(--deep-green)" opacity=".75"/>
      <circle cx="1095" cy="612" r="76" fill="var(--deep-green)"/>
      <polygon class="band-cover-footer" points="608,800 1175,735 1175,898 608,898" fill="var(--bark)"/>

      <circle cx="740" cy="405" r="77" fill="var(--paper)"/>
      <circle cx="740" cy="405" r="71" fill="#7f9a5a" role="img" aria-label="Photo: hikers climbing a steep grassy slope"/>
      <circle cx="757" cy="580" r="77" fill="var(--paper)"/>
      <circle cx="757" cy="580" r="71" fill="#a3a68a" role="img" aria-label="Photo: group doing a plank challenge outdoors"/>
      <circle cx="925" cy="665" r="88" fill="var(--paper)"/>
      <circle cx="925" cy="665" r="82" fill="var(--sky)" role="img" aria-label="Photo: sea kayakers paddling on blue water"/>
      <circle cx="937" cy="466" r="152" fill="var(--paper)"/>
      <circle cx="937" cy="466" r="145" fill="#8c7a66" role="img" aria-label="Photo: smiling team lying together on the grass"/>
    </g>
  </svg>

  <p class="quote"><span class="mark mark-open">“</span>I work from an Eco-Systemic approach, using tools from a variety of theories depending on fit with a client. While I am not tied to a specific theory I have experience with cognitive behavioural therapy, gestalt therapy, narrative therapy and solution focused therapy. My approach is humanistic and person centred, which means I hold the belief that you are the expert of your own life and have all the resources you need to live in the manner that fullfils you. I see my role in your process being to helping you cultivate resources by providing, information, strategies, and an alternative perspective. <span class="mark">”</span></p>
  <p class="founder-name">Maren Holloway</p>
  <p class="founder-role">Founder of Cobaltine Outdoor</p>

  <h2 class="contact-title">Contact Us</h2>
  <p class="contact-lines">Email: <strong>info@cobaltineoutdoor.com</strong><br>Call: <strong>(604) 555-0147</strong></p>
  <p class="web-address">www.cobaltineoutdoor.com</p>

  <div class="brand-mark">
    <span class="brand-dot"></span>
    <span class="brand-name">Cobaltine<br>Outdoor</span>
  </div>

  <h1 class="cover-title">Cobaltine Outdoor</h1>
  <p class="cover-tagline">Combining adventure activities, psychotherapy and experiential<br>education to facilitate personal transformation</p>
</div>
</body>
</html>
```